Corvane Nightclub Flyer (Updated)

Flyer for facebook, square is fine, or rectangular. Here is the text:
CORVANE
Nightclub + Lounge
presents

HALO THURSDAY
Nov 29 2018

CLUB FLOOR:
GLEN B2B ROBBY
FREDERICK TALAVERO

LOUNGE:
CARL B2B MY COUSIN
ROCKET JULES

Powered by KESTA Acoustics
4217 6th Street 21+ 9pm-2am
corvanevenuehall.com for VIP booth inquiries

Target Market(s)

Nightclub

Industry/Entity Type

Night Club

Font styles to use
Sans Serif

Colors

Designer to choose colors to be used in the design.

Requirements
Must have
• All the text listed, and plz keep the theme of the attached files. We want to stay consistent with the Corvane brand
Nice to have
• Try to stay with the theme from the attachments
Should not have
• Dont' stray to far from the general theme we have from the attachments

```html
<!DOCTYPE html>
<html lang="en">
<head>
<meta charset="utf-8">
<title>Corvane Nightclub + Lounge – Halo Thursday</title>
<link href="https://fonts.googleapis.com/css2?family=Bodoni+Moda:wght@400&family=Cinzel:wght@700&family=Montserrat:wght@300;400;500;700;800&display=swap" rel="stylesheet">
<style>
  :root {
    --bg: #000000;
    --ink: #ffffff;
    --gold: #c49a5e;
    --gold-soft: #b08a55;
    --gold-light: #f3d29a;
    --gold-dark: #8f6a3d;
    --panel: #0a0a0a;
  }
  html, body {
    margin: 0;
    padding: 0;
    width: 1200px;
    height: 1200px;
    overflow: hidden;
    background: var(--bg);
  }
  .flyer {
    position: relative;
    width: 1200px;
    height: 1200px;
    background: radial-gradient(circle at 50% 50%, #141414 0%, #050505 70%, #000 100%);
    color: var(--ink);
    font-family: "Montserrat", sans-serif;
    overflow: hidden;
  }
  .frame {
    position: absolute;
    inset: 0;
  }
  .center {
    position: absolute;
    left: 0;
    width: 100%;
    text-align: center;
    margin: 0;
  }
  .brand-name {
    top: 100px;
    font-family: "Bodoni Moda", serif;
    font-weight: 400;
    font-size: 122px;
    line-height: 1;
    letter-spacing: 2px;
  }
  .brand-sub {
    top: 228px;
    font-weight: 300;
    font-size: 34px;
    letter-spacing: 5px;
    line-height: 1;
  }
  .presents {
    top: 300px;
    color: var(--gold);
    font-weight: 300;
    font-size: 28px;
    letter-spacing: 5px;
    line-height: 1;
  }
  .event-banner {
    position: absolute;
    left: 324px;
    top: 378px;
    width: 552px;
    height: 78px;
    background: linear-gradient(90deg, var(--gold-dark) 0%, #c59d62 30%, var(--gold-light) 62%, #b58d57 100%);
    display: flex;
    align-items: center;
    justify-content: center;
    font-weight: 700;
    font-size: 53px;
    letter-spacing: 1px;
    color: var(--ink);
  }
  .event-date {
    top: 474px;
    color: var(--gold);
    font-weight: 400;
    font-size: 22px;
    letter-spacing: 4px;
    line-height: 1;
  }
  .stage {
    position: absolute;
    left: 324px;
    width: 552px;
    height: 122px;
    border: 1.5px solid var(--gold-soft);
    box-sizing: border-box;
  }
  .stage--club { top: 562px; }
  .stage--lounge { top: 774px; }
  .stage-label {
    position: absolute;
    left: 135px;
    top: -28px;
    width: 282px;
    height: 56px;
    box-sizing: border-box;
    background: var(--panel);
    border: 1.5px solid var(--gold-soft);
    display: flex;
    align-items: center;
    justify-content: center;
    font-family: "Cinzel", serif;
    font-weight: 700;
    font-size: 34px;
    color: var(--gold);
    letter-spacing: 0.5px;
  }
  .lineup {
    position: absolute;
    left: 0;
    right: 0;
    top: 44px;
    text-align: center;
    font-weight: 400;
    font-size: 22px;
    line-height: 30px;
    letter-spacing: 0.3px;
  }
  .divider {
    position: absolute;
    left: 108px;
    top: 942px;
    width: 984px;
    height: 1.5px;
    background: var(--gold-soft);
  }
  .vip {
    top: 967px;
    color: var(--gold);
    font-weight: 300;
    font-size: 31px;
    letter-spacing: 3.2px;
    line-height: 1;
  }
  .powered {
    top: 1036px;
    display: flex;
    justify-content: center;
    align-items: center;
    gap: 10px;
    font-size: 24px;
    font-weight: 400;
    line-height: 1;
  }
  .powered .sponsor {
    font-weight: 800;
    font-size: 50px;
    letter-spacing: 2px;
  }
  .venue-info {
    top: 1098px;
    font-size: 24px;
    font-weight: 400;
    line-height: 1;
  }
</style>
</head>
<body>
<main class="flyer">
  <svg class="frame" width="1200" height="1200" viewBox="0 0 1200 1200" aria-hidden="true">
    <defs>
      <linearGradient id="frameGold" x1="0" y1="0" x2="1" y2="1">
        <stop offset="0" stop-color="#d9b178"/>
        <stop offset="0.5" stop-color="#9d7748"/>
        <stop offset="1" stop-color="#d9b178"/>
      </linearGradient>
    </defs>
    <path fill="none" stroke="url(#frameGold)" stroke-width="3"
      d="M78 42 H1122 V60 H1140 V78 H1158 V1122 H1140 V1140 H1122 V1158 H78 V1140 H60 V1122 H42 V78 H60 V60 H78 Z"/>
    <rect x="58" y="58" width="1084" height="1084" fill="none" stroke="url(#frameGold)" stroke-width="1.5"/>
  </svg>

  <h1 class="center brand-name">CORVANE</h1>
  <div class="center brand-sub">NIGHTCLUB + LOUNGE</div>
  <div class="center presents">presents</div>

  <div class="event-banner">HALO THURSDAY</div>
  <div class="center event-date">NOV 29 2018</div>

  <section class="stage stage--club">
    <div class="stage-label">CLUB FLOOR</div>
    <div class="lineup">GLEN B2B ROBBY<br>FREDERICK TALAVERO</div>
  </section>

  <section class="stage stage--lounge">
    <div class="stage-label">LOUNGE</div>
    <div class="lineup">CARL B2B MY COUSIN<br>ROCKET JULES</div>
  </section>

  <div class="divider"></div>
  <div class="center vip">CORVANEVENUEHALL.COM FOR VIP BOOTH INQUIRIES</div>
  <div class="center powered"><span>Powered by</span><span class="sponsor">KESTA</span><span>Acoustics</span></div>
  <div class="center venue-info">4217 6th Street 21+ 9pm-2am</div>
</main>
</body>
</html>
```